Business card design needed

I would like a one sided black business card with the information provided above. Refer to my website www.lobcrafttennis.com.au for an example of colors I have used for my site, would like to keep this consistent for my business cards also, I will upload my logo below.

I am a new small business that provides tennis customers with racquet re stringing, tennis strings and accessories.

Industry/Entity Type

Small Business

Contact Information for Business Card

Lob Craft Tennis

Dennis Morrow
Managing Director

lobcrafttennis@mailbay.com
www.lobcrafttennis.com.au
0412 695 203

Racquet Restringing/Tennis Strings/Accessories

Requirements
Must have
• Must have my logo and card must be black

```html
<!DOCTYPE html>
<html lang="en">
<head>
<meta charset="utf-8">
<title>Lob Craft Tennis – Business Card</title>
<link rel="stylesheet" href="https://fonts.googleapis.com/css2?family=Source+Sans+3:wght@400;600;700&display=swap">
<style>
  :root {
    --page-bg: #e9e6e2;
    --card-black: #050505;
    --lime: #b6d334;
    --white: #ffffff;
  }
  * { box-sizing: border-box; margin: 0; padding: 0; }
  html, body {
    width: 1200px;
    height: 750px;
    overflow: hidden;
    background: var(--page-bg);
    font-family: "Source Sans 3", "Myriad Pro", sans-serif;
  }
  .card {
    position: absolute;
    left: 75px;
    top: 75px;
    width: 1050px;
    height: 598px;
    background: var(--card-black);
    border-radius: 38px;
    color: var(--white);
  }
  .brand {
    position: absolute;
    left: 0;
    right: 0;
    top: 118px;
    display: flex;
    justify-content: center;
    align-items: center;
    gap: 18px;
  }
  .brand-dot {
    width: 40px;
    height: 40px;
    border-radius: 50%;
    background: var(--lime);
  }
  .brand-name {
    font-size: 56px;
    font-weight: 700;
    color: var(--lime);
    letter-spacing: 1px;
    line-height: 1;
  }
  .services {
    position: absolute;
    left: 0;
    right: 0;
    top: 287px;
    display: flex;
    justify-content: center;
    gap: 18px;
    list-style: none;
    font-size: 29px;
    line-height: 1;
  }
  .services li::before {
    content: "";
    display: inline-block;
    width: 8px;
    height: 8px;
    background: var(--white);
    margin-right: 12px;
    vertical-align: 6px;
  }
  .person {
    position: absolute;
    left: 0;
    right: 0;
    top: 438px;
    text-align: center;
    color: var(--lime);
    line-height: 1;
  }
  .person-name { font-size: 33px; font-weight: 700; }
  .person-role { font-size: 26px; font-weight: 400; margin-left: 10px; }
  .contacts {
    position: absolute;
    left: 0;
    right: 0;
    top: 509px;
    display: flex;
    justify-content: center;
    gap: 36px;
    list-style: none;
    font-size: 24px;
    line-height: 1;
  }
  .contacts li { display: flex; align-items: center; gap: 10px; }
  .contacts svg { width: 22px; height: 22px; fill: var(--lime); flex: none; }
</style>
</head>
<body>
  <main class="card">
    <div class="brand">
      <span class="brand-dot"></span>
      <span class="brand-name">Lob Craft Tennis</span>
    </div>

    <ul class="services">
      <li>Racquet Restringing</li>
      <li>Tennis Strings</li>
      <li>Accessories</li>
    </ul>

    <p class="person">
      <span class="person-name">Dennis Morrow,</span><span class="person-role">Managing Director</span>
    </p>

    <ul class="contacts">
      <li>
        <svg viewBox="0 0 24 24" aria-hidden="true"><path d="M3 8c0-2 4-4 9-4s9 2 9 4v2h-5V8c-1-.6-2.5-1-4-1s-3 .4-4 1v2H3zM6 12h12l2 8H4z M10 14a2 2 0 1 0 4 0 2 2 0 1 0-4 0" fill-rule="evenodd"/></svg>
        <span>0412 695 203</span>
      </li>
      <li>
        <svg viewBox="0 0 24 24" aria-hidden="true"><path d="M2 5h20v14H2z M4 7v.5l8 6 8-6V7z M4 10v7h16v-7l-8 6z" fill-rule="evenodd"/></svg>
        <span>lobcrafttennis@mailbay.com</span>
      </li>
      <li>
        <svg viewBox="0 0 24 24" aria-hidden="true"><circle cx="12" cy="12" r="10"/><path d="M2 12h20M12 2c3 3 3 17 0 20M12 2c-3 3-3 17 0 20M4 7h16M4 17h16" stroke="#050505" stroke-width="1.2" fill="none"/></svg>
        <span>www.lobcrafttennis.com.au</span>
      </li>
    </ul>
  </main>
</body>
</html>
```